Creative Flyer Design Project

I want to create a flyer. I have attached wireframe (wireframe.png) of flyer which gives you much needed idea regarding flyer content. I have attached few images from our portfolio which can be used while designing a flyer.

I would like you to show me the extreme creativity and capability in delivering world class flyer design.

No heavy graphics needed. I want extremely clean and professional flyer using icons, colors and highlighted text/headings.

I will be requiring multiple formats of flyer such as .ai/.png/.psd/pdf.

Size of flyer: Standard A4 size OR Height is at discretion of designer. The width must be below 780 px.

Fonts to be used: Web 2.0 fonts needed. Must drive message clearly.

*** Long term association oppurtunity exists for the right creative designers for direct work

Target Market(s)

Business owners

Industry/Entity Type

Work

Requirements
Should not have
• Cartoonish or cheap graphics

```html
<!DOCTYPE html>
<html lang="en">
<head>
<meta charset="utf-8">
<title>Custom Graphic Design Flyer</title>
<link rel="stylesheet" href="https://fonts.googleapis.com/css2?family=Ubuntu:wght@400;500;700&family=Tinos&display=swap">
<style>
:root{
  --stage:#2a2d33;
  --stage-light:#3a3e46;
  --gold:#c9a400;
  --gold-dark:#a38600;
  --gold-text:#a38d00;
  --ink:#1d1d1d;
  --white:#ffffff;
  --paper:#ffffff;
  --paper-fade:#ececec;
}
*{margin:0;padding:0;box-sizing:border-box}
html,body{width:1200px;height:1000px;overflow:hidden}
body{background:radial-gradient(ellipse at center,var(--stage-light) 0%,var(--stage) 70%);font-family:"Ubuntu",sans-serif;color:var(--ink);position:relative}
.flyer{position:absolute;left:275px;top:40px;width:650px;height:920px;background:linear-gradient(180deg,var(--paper) 40%,var(--paper-fade) 100%);overflow:hidden}
.abs{position:absolute}
.header-band{left:0;top:0;width:650px;height:270px}
.site-logo{left:30px;top:30px;width:180px;height:77px;background:#000;color:#d8d8d8;font-family:"Tinos",serif;font-size:27px;display:flex;align-items:center;justify-content:center;letter-spacing:.5px}
.headline{left:238px;top:39px;color:var(--white);font-weight:500;white-space:nowrap}
.headline .small{font-size:21px;font-weight:700;display:block}
.headline .big{font-size:33px;display:block;margin-top:-3px;letter-spacing:.3px}
.thumb{top:117px;width:126px;height:125px;box-shadow:4px 4px 0 var(--gold-dark)}
.label{background:var(--gold);color:var(--white);font-weight:700;font-size:12px;line-height:13px;padding:3px 8px;white-space:nowrap}
.list{list-style:none;font-size:12px;line-height:14.5px;white-space:nowrap}
.list li{padding-left:14px;position:relative}
.list li::before{content:"+";position:absolute;left:0;top:0;font-weight:700}
.services-title{left:0;width:650px;top:472px;text-align:center;color:var(--gold-text);font-size:21.6px;font-weight:700;white-space:nowrap}
.partner{left:31px;top:744px;font-size:14px;font-weight:500;white-space:nowrap}
.discount-tab{left:0;top:765px;width:352px;height:47px;background:var(--gold);border-radius:0 24px 0 0;padding:6px 0 0 31px;font-weight:700;font-size:13.5px;color:var(--ink);white-space:nowrap}
.discount-tab .code{display:block;text-align:right;padding-right:18px;color:var(--white);font-size:13px}
.footer{left:0;top:812px;width:650px;height:108px;background:var(--gold)}
.contact{color:var(--white);font-size:15px;font-weight:700;display:flex;align-items:center;gap:8px;white-space:nowrap}
.contact.web{font-size:16px}
.contact.sm{font-size:11px;font-weight:500}
.chip{width:31px;height:31px;background:var(--white);border-radius:4px}
</style>
</head>
<body>
<div class="flyer">
  <svg class="abs header-band" viewBox="0 0 650 270">
    <path d="M0 0H650V268H40Q0 268 0 230Z" fill="var(--gold-dark)"/>
    <path d="M0 0H650V256H46Q8 256 0 222Z" fill="var(--gold)"/>
  </svg>
  <div class="abs site-logo">SITE LOGO</div>
  <div class="abs headline"><span class="small">100% Custom graphic design at the</span><span class="big">most affordable prices</span></div>

  <div class="abs thumb" style="left:30px;background:linear-gradient(180deg,#3b5a99 0 8%,#1c1c1c 8% 40%,#f2f2f2 40%)" role="img" aria-label="Portfolio sample: social network page design"></div>
  <div class="abs thumb" style="left:185px;background:#3e3e3e" role="img" aria-label="Portfolio sample: two door hanger designs for window and attic installation"></div>
  <div class="abs thumb" style="left:340px;background:linear-gradient(180deg,#1a1a1a,#5a1010)" role="img" aria-label="Portfolio sample: three trade show banner stands"></div>
  <div class="abs thumb" style="left:495px;background:linear-gradient(180deg,#ffffff 0 65%,#111 65% 80%,#0c3b0c 80%)" role="img" aria-label="Portfolio sample: brand identity for a green company"></div>

  <svg class="abs" style="left:27px;top:283px" width="30" height="30" viewBox="0 0 30 30"><circle cx="15" cy="15" r="15" fill="var(--gold)"/><path d="M15 7V23M7 15H23" stroke="#fff" stroke-width="4"/></svg>
  <div class="abs label" style="left:62px;top:282px;padding:3px 6px;font-size:11.5px">Benefits you get by dealing with<br>aaaaaaaaaaaaa.com</div>
  <ul class="abs list" style="left:31px;top:316px">
    <li>Creatively crafted functional designs</li>
    <li>Highly affordable pricing</li>
    <li>Multiple variations of designs submitted</li>
    <li>Variations open to revisions</li>
    <li>Guaranteed 48 hours delivery</li>
    <li>30000+ ready also available, all open for</li>
    <li>100% customization at no extra cost</li>
  </ul>

  <svg class="abs" style="left:313px;top:282px" width="30" height="30" viewBox="0 0 30 30"><circle cx="15" cy="15" r="15" fill="var(--gold)"/><path d="M8 10L13 15L8 20M15 10L20 15L15 20" stroke="#fff" stroke-width="2.5" fill="none"/></svg>
  <div class="abs label" style="left:348px;top:290px">Our design process</div>
  <ul class="abs list" style="left:320px;top:315px">
    <li>Careful analysis of your individual &amp; business needs</li>
    <li>Creation of rough hand drawn sketches</li>
    <li>Analyzing sketches &amp; shortlisting them</li>
    <li>Conversion of shortlisted hand drawn sketches<br>to digital formats</li>
    <li>Submission of multiple variations of designs<br>to choose from</li>
    <li>Feedback / suggestions rounds to give<br>final shape to your design</li>
    <li>Delivery of design in multiple digital formats</li>
  </ul>

  <div class="abs services-title">Our services are available in 36 design categories</div>

  <svg class="abs" style="left:27px;top:508px" width="30" height="30" viewBox="0 0 30 30"><circle cx="15" cy="15" r="15" fill="var(--gold)"/><circle cx="15" cy="15" r="10" fill="none" stroke="#fff" stroke-width="1.5"/><circle cx="15" cy="10.5" r="2" fill="#fff"/><rect x="13" y="13.5" width="4" height="8" fill="#fff"/></svg>
  <div class="abs label" style="left:62px;top:516px">CORPORATE IDENTITY</div>
  <ul class="abs list" style="left:31px;top:541px">
    <li>Logo design</li><li>Stationary design</li><li>Business card design</li><li>Envelope design</li><li>Letterhead design</li><li>Presentation folder design</li><li>Power point template design</li>
  </ul>

  <svg class="abs" style="left:246px;top:508px" width="30" height="30" viewBox="0 0 30 30"><circle cx="15" cy="15" r="15" fill="var(--gold)"/><g fill="none" stroke="#fff" stroke-width="1.3"><circle cx="15" cy="15" r="10"/><ellipse cx="15" cy="15" rx="4.5" ry="10"/><path d="M5 15H25M7 10H23M7 20H23"/></g></svg>
  <div class="abs label" style="left:281px;top:516px">WEB DESIGN</div>
  <ul class="abs list" style="left:251px;top:541px">
    <li>Landing page design</li><li>Web page design</li><li>Ecommerce design</li><li>Blog design</li><li>CMS website design</li><li>Newsletter design</li><li>Banner ad design</li><li>Circlebook page design</li><li>Chirper page design</li><li>Vidstream page design</li><li>Spaceloop page design</li>
  </ul>

  <svg class="abs" style="left:419px;top:508px" width="30" height="30" viewBox="0 0 30 30"><circle cx="15" cy="15" r="15" fill="var(--gold)"/><rect x="10" y="7" width="10" height="6" fill="#fff"/><rect x="7" y="13" width="16" height="7" fill="#fff"/><rect x="10" y="18" width="10" height="5" fill="#fff" stroke="var(--gold)"/></svg>
  <div class="abs label" style="left:454px;top:516px">GRAPHICS / PRINT DESIGN</div>
  <ul class="abs list" style="left:424px;top:541px">
    <li>T-shirt design</li><li>Brochure design</li><li>Poster design</li><li>Postcard design</li><li>Flyer design</li><li>Book cover design</li><li>Label / Sticker design</li><li>CD cover design</li><li>Trade show display</li><li>Signage design</li><li>Newspaper ad design</li><li>Greeting card &nbsp;/ Invitation design</li><li>Packaging design</li><li>Vehicle wrap design</li><li>Shopping bag design</li><li>Door hanger design</li><li>Certificate design</li>
  </ul>

  <svg class="abs" style="left:56px;top:654px" width="86" height="86" viewBox="0 0 86 86"><circle cx="43" cy="43" r="41" fill="none" stroke="#222" stroke-width="2.5"/><circle cx="43" cy="43" r="27" fill="none" stroke="#222" stroke-width="2"/></svg>

  <div class="abs partner">Prefferred partner for 5000+ individuals &amp; businesses</div>
  <div class="abs discount-tab">21% Special discount for our warrior members<span class="code">Use &gt;&gt; zzzzzzz2013</span></div>

  <div class="abs footer"></div>
  <div class="abs contact" style="left:30px;top:824px">
    <svg width="20" height="24" viewBox="0 0 20 24"><path d="M5 1L9 6L6 9Q8 15 12 18L15 15L19 19L16 23Q6 21 2 6Z" fill="#fff"/></svg>: +11 88888 99999</div>
  <div class="abs contact web" style="left:30px;top:862px">
    <svg width="20" height="26" viewBox="0 0 20 26"><rect x="2" y="1" width="16" height="24" rx="8" fill="#fff"/><path d="M2 11H18M10 1V11" stroke="var(--gold)" stroke-width="1.5"/></svg>: www.aaaaaaaaaaaaa.com</div>
  <div class="abs contact sm" style="left:298px;top:820px"><span class="chip"></span>xxxxxxxxxxxxxxxxx</div>
  <div class="abs contact sm" style="left:298px;top:858px"><span class="chip"></span>info@xxxxxxxxxxx.com</div>
  <div class="abs contact sm" style="left:500px;top:820px"><span class="chip"></span>yyyyyyyyyyy</div>
  <div class="abs contact sm" style="left:500px;top:858px"><span class="chip"></span>zzzzzzzzzzz</div>
</div>
</body>
</html>
```